Professional Single Page Website Design for Velloway Advisory

Velloway Advisory is a new business consultancy specializing in providing expert services to small businesses, primarily in the brick-and-mortar retail and food service sectors. We offer a range of services including franchise development and launch, due diligence, and construction management.

Currently, we have a basic website set up at www.vellowayadvisory.example, but we need a professional touch to enhance its design and functionality.

Project Requirements:
- Single Page Design: For now, we need a single page design that effectively showcases who we are, our services, and contact information.
- Future Expansion: The design should be flexible and scalable for future expansion to include additional pages like specific service offerings, about us, and a dedicated contact page.
- Design Aesthetic: We are looking for a modern yet professional design that aligns with our brand identity.
- Logo: We have a logo that we like, which was also sourced from Pixel Forum. The logo files are attached to this project brief.

Key Sections to Include:
- Hero Section: An engaging introduction to Velloway Advisory with a strong visual impact.
- About Us: A brief overview of who we are and our mission.
- Team: Section for the profiles of the two principals.
- Services: A clear and concise presentation of our services, including franchise development, due diligence, and construction management.
- Contact Information: Easy-to-find contact details, including a form for inquiries.
- Call to Action: Encouraging visitors to get in touch with us for consultations or further information.

Design Considerations:
- Ensure the design is responsive and mobile-friendly.
- Include high-quality images and icons that complement our services and industry.
- We do not need development services, this is only a design project.

```html
<!DOCTYPE html>
<html lang="en">
<head>
<meta charset="utf-8">
<title>Velloway Advisory</title>
<link href="https://fonts.googleapis.com/css2?family=Poppins:wght@300;400;500;600;700&display=swap" rel="stylesheet">
<style>
:root{
  --page:#eef5f1;
  --navy:#0f1847;
  --ink:#11161f;
  --muted:#6b7280;
  --mint:#9dd3bc;
  --mint-soft:#d3e9df;
  --mint-text:#7cc4a3;
  --green-deep:#0b3f28;
  --green:#0c7a47;
  --white:#ffffff;
}
*{margin:0;padding:0;box-sizing:border-box}
html,body{width:1200px;height:4125px;overflow:hidden}
body{background:var(--page);font-family:"Poppins",sans-serif;color:var(--navy);position:relative}
.abs{position:absolute}
a{text-decoration:none;color:inherit}

/* brand */
.brand{display:flex;align-items:center;gap:12px}
.brand-dot{width:60px;height:60px;border-radius:50%;background:var(--mint)}
.brand-name{font-weight:600;font-size:22px;line-height:24px}

/* hero */
.hero{left:16px;top:16px;width:1168px;height:590px;border-radius:26px;overflow:hidden;
  background:linear-gradient(100deg,#0a5a36 0%,#0d7a48 45%,#13a05c 75%,#0d6f42 100%)}
.hero .brand{position:absolute;left:112px;top:16px;color:var(--white)}
.nav{position:absolute;right:112px;top:29px;display:flex;align-items:center;gap:32px;color:var(--white);font-size:14px}
.nav .btn-contact{background:var(--white);color:var(--mint-text);padding:14px 30px;border-radius:4px;font-size:14px;letter-spacing:.5px;margin-left:2px}
.hero h1{position:absolute;left:114px;top:170px;font-size:48px;line-height:58px;font-weight:600;color:var(--white)}
.hero .kicker{position:absolute;left:114px;top:305px;font-size:18px;color:var(--white);font-weight:500}
.hero .kicker b{color:#a9e2c5;font-weight:500}
.hero p{position:absolute;left:114px;top:350px;width:530px;font-size:13px;line-height:22px;color:#e4f4ec}
.btn{display:inline-block;background:var(--mint);color:var(--white);font-size:14px;letter-spacing:.4px;text-align:center;border-radius:4px}
.hero .btn{position:absolute;left:114px;top:449px;width:156px;line-height:48px}

/* about */
.about-visual{left:48px;top:674px;width:513px;height:513px}
.eyebrow{font-size:15px;font-weight:500;letter-spacing:2px;color:var(--mint-text)}
.about-text{left:619px;top:706px;width:430px}
.about-text h2{font-size:54px;line-height:62px;font-weight:600;margin-top:6px}
.about-text p{font-size:13px;line-height:21.7px;color:var(--muted);margin-top:22px}
.about-text .btn{width:197px;line-height:48px;margin-top:40px}

/* services */
.watermark{font-weight:500;color:#e3ede8;white-space:nowrap;text-align:center;left:0;width:1200px}
.section-head{left:0;width:1200px;text-align:center}
.section-head h2{font-size:52px;font-weight:600;line-height:62px;color:var(--ink)}
.card{background:var(--white);border-radius:12px;box-shadow:0 5px 0 var(--mint-soft);width:300px;height:272px;text-align:center;padding:18px 22px 0}
.card .icon{width:50px;height:50px;display:block;margin:0 auto}
.card h3{font-size:18px;line-height:24px;font-weight:600;margin-top:6px;color:var(--navy)}
.card p{font-size:13px;line-height:21px;color:var(--muted);margin-top:10px}
.card .more{position:absolute;right:34px;bottom:22px;font-size:14px;line-height:18px;color:var(--mint-text);display:flex;align-items:center;gap:6px}
.card .more svg{width:18px;height:10px;display:block}

/* cta */
.cta{left:16px;top:2074px;width:1168px;height:560px;border-radius:26px;overflow:hidden;
  background:linear-gradient(120deg,#123f2c 0%,#1d6a48 50%,#0f3a26 100%);text-align:center;color:var(--white)}
.cta h2{margin-top:124px;font-size:50px;line-height:64px;font-weight:600}
.cta p{width:560px;margin:36px auto 0;font-size:13px;line-height:21.5px;color:#e2efe8}
.cta .btn{width:156px;line-height:48px;margin-top:50px}

/* team */
.member{top:2871px;width:452px;height:260px;background:var(--white);border-radius:12px;box-shadow:5px 4px 0 var(--mint-soft);overflow:hidden}
.member .photo{position:absolute;left:0;top:0;width:202px;height:260px}
.member .contacts{position:absolute;left:70px;top:222px;display:flex;gap:8px}
.member .contacts span{width:26px;height:26px;border-radius:50%;background:var(--mint);display:flex;align-items:center;justify-content:center}
.member .info{position:absolute;left:230px;top:28px;width:200px}
.member h3{font-size:24px;font-weight:600;line-height:30px}
.member .role{font-size:12px;color:var(--mint-text);font-weight:500;letter-spacing:.5px;margin-top:2px}
.member p{font-size:13px;line-height:21.5px;color:var(--muted);margin-top:14px}

/* contact */
.contact{left:16px;top:3224px;width:837px;height:562px;border-radius:26px;overflow:hidden;
  background:linear-gradient(120deg,#0b3a26 0%,#0f5a39 55%,#0a3323 100%);color:var(--white)}
.contact .eyebrow{position:absolute;left:114px;top:82px;color:var(--white)}
.contact h2{position:absolute;left:114px;top:104px;font-size:50px;font-weight:600;line-height:60px}
.field{position:absolute;background:var(--white);border-radius:3px;font-size:13px;color:#9aa0a6;padding:0 16px;display:flex;align-items:center}
.contact .submit{position:absolute;left:114px;top:433px;width:114px;line-height:48px;font-size:14px}
.map{left:658px;top:3253px;width:526px;height:504px;border-radius:26px;border:6px solid var(--white);
  background:linear-gradient(160deg,#efe3c4 0%,#e9dcb9 45%,#b9d7c3 75%,#e7dbb9 100%);box-shadow:0 0 0 4px var(--green-deep)}

/* footer */
.footer-brand{left:128px;top:3866px;color:var(--navy)}
.copy{left:130px;top:3982px;font-size:13px;color:var(--ink)}
.copy span{color:var(--mint-text)}
.fcol h4{font-size:13px;font-weight:600;letter-spacing:1.5px;color:var(--ink)}
.fcol li{list-style:none;font-size:13px;color:var(--muted);line-height:30px}
.fcol .line{display:flex;gap:6px;font-size:13px;color:var(--muted);line-height:18px;margin-top:12px}
.social{display:flex;gap:12px;margin-top:20px}
.social span{width:18px;height:18px;border-radius:50%;border:1px solid var(--mint)}
</style>
</head>
<body>

<header class="hero abs">
  <div class="brand"><span class="brand-dot"></span><span class="brand-name">Velloway<br>Advisory</span></div>
  <nav class="nav"><a>About</a><a>Services</a><a>Team</a><a class="btn-contact">CONTACT</a></nav>
  <h1>Building Success<br>in Southern California</h1>
  <div class="kicker"><b>Expertise at Every Step:</b> From Planning to Execution</div>
  <p>At Velloway, we combine innovative strategies with local expertise to support your commercial real estate projects. From restaurants to retail, we turn your goals into success. Partner with us and grow.</p>
  <a class="btn">GET STARTED</a>
</header>

<svg class="abs about-visual" viewBox="0 0 513 513" role="img" aria-label="Hand drawing a glowing maze path from problem to solution">
  <defs><linearGradient id="aboutFill" x1="0" y1="0" x2="1" y2="1"><stop offset="0" stop-color="#3a4f63"/><stop offset=".5" stop-color="#1d2c3c"/><stop offset="1" stop-color="#0e1620"/></linearGradient></defs>
  <rect x="75" y="75" width="363" height="363" rx="110" transform="rotate(45 256.5 256.5)" fill="#d0e6dc"/>
  <rect x="115" y="115" width="283" height="283" rx="85" transform="rotate(45 256.5 256.5)" fill="url(#aboutFill)"/>
</svg>

<section class="about-text abs">
  <div class="eyebrow">ABOUT</div>
  <h2>Velloway<br>Advisory</h2>
  <p>Welcome to Velloway Advisory, your trusted partner in navigating the complexities of the real estate and small business markets. Founded by industry veterans Rafael Montoya and Daniel Oh, we specialize in providing comprehensive services tailored to the unique needs of our clients. Whether you're a franchisee, a new restaurant owner, or a commercial real estate investor, our expertise in due diligence, construction management, and investment property evaluation ensures you make informed, strategic decisions.</p>
  <a class="btn">CONTACT US NOW</a>
</section>

<div class="abs watermark" style="top:1195px;font-size:170px;line-height:200px">Services</div>
<div class="abs section-head" style="top:1270px"><div class="eyebrow">SERVICES</div><h2>Velloway Services</h2></div>

<article class="card abs" style="left:130px;top:1399px">
  <svg class="icon" viewBox="0 0 54 54" fill="none" stroke="#7cc4a3" stroke-width="1.6"><circle cx="27" cy="27" r="7"/><circle cx="27" cy="8" r="4"/><circle cx="27" cy="46" r="4"/><circle cx="9" cy="18" r="4"/><circle cx="45" cy="18" r="4"/><circle cx="9" cy="36" r="4"/><circle cx="45" cy="36" r="4"/><path d="M27 12v8M27 34v8M12 20l9 4M42 20l-9 4M12 34l9-4M42 34l-9-4"/></svg>
  <h3>Franchise<br>Development &amp; Launch</h3>
  <p>Comprehensive franchise setup from evaluation to launch for scalable business growth.</p>
  <span class="more">READ MORE <svg viewBox="0 0 18 10" fill="none" stroke="#7cc4a3" stroke-width="1.5"><path d="M0 5h16M12 1l4 4-4 4"/></svg></span>
</article>
<article class="card abs" style="left:451px;top:1399px">
  <svg class="icon" viewBox="0 0 54 54" fill="none" stroke="#7cc4a3" stroke-width="1.6"><circle cx="27" cy="27" r="16"/><circle cx="27" cy="27" r="10"/><path d="M22 27l4 4 7-8M27 5v6M27 43v6M5 27h6M43 27h6M12 12l4 4M38 38l4 4M42 12l-4 4M12 42l4-4"/></svg>
  <h3 style="margin-top:12px">Due Diligence Services</h3>
  <p>Conducting thorough due diligence for business and property transactions to identify potential risks and liabilities.</p>
  <span class="more">READ MORE <svg viewBox="0 0 18 10" fill="none" stroke="#7cc4a3" stroke-width="1.5"><path d="M0 5h16M12 1l4 4-4 4"/></svg></span>
</article>
<article class="card abs" style="left:772px;top:1399px">
  <svg class="icon" viewBox="0 0 54 54" fill="none" stroke="#7cc4a3" stroke-width="1.6"><rect x="18" y="10" width="18" height="30"/><path d="M22 16h4M28 16h4M22 22h4M28 22h4M22 28h4M28 28h4M8 40h38M12 40v8M42 40v8M24 40v-6h6v6"/></svg>
  <h3>Building &amp; Construction<br>Management</h3>
  <p>Conducting thorough due diligence for business and property transactions to identify potential risks and liabilities.</p>
  <span class="more">READ MORE <svg viewBox="0 0 18 10" fill="none" stroke="#7cc4a3" stroke-width="1.5"><path d="M0 5h16M12 1l4 4-4 4"/></svg></span>
</article>
<article class="card abs" style="left:284px;top:1692px">
  <svg class="icon" viewBox="0 0 54 54" fill="none" stroke="#7cc4a3" stroke-width="1.6"><rect x="8" y="8" width="30" height="38"/><path d="M14 22l9-7 9 7M16 20v10h14V20M14 36h18M14 41h12"/><circle cx="40" cy="38" r="7"/><path d="M45 43l5 5"/></svg>
  <h3>Investment Property<br>Evaluation</h3>
  <p>Providing detailed analysis of potential investment properties, including profitability forecasts and risk assessments.</p>
  <span class="more">READ MORE <svg viewBox="0 0 18 10" fill="none" stroke="#7cc4a3" stroke-width="1.5"><path d="M0 5h16M12 1l4 4-4 4"/></svg></span>
</article>
<article class="card abs" style="left:605px;top:1692px">
  <svg class="icon" viewBox="0 0 54 54" fill="none" stroke="#7cc4a3" stroke-width="1.6"><circle cx="22" cy="30" r="15"/><path d="M12 34l6-6 5 4 9-10M33 41l8 8M30 12l18-6M42 5l6 1-1 6"/></svg>
  <h3>Market Analysis &amp;<br>Feasibility Studies</h3>
  <p>Conducting comprehensive market research to assess the viability of real estate.</p>
  <span class="more">READ MORE <svg viewBox="0 0 18 10" fill="none" stroke="#7cc4a3" stroke-width="1.5"><path d="M0 5h16M12 1l4 4-4 4"/></svg></span>
</article>

<section class="cta abs" role="img" aria-label="Team planning around a table covered with documents, green tinted">
  <h2>Unlock Your Business<br>Potential Today!</h2>
  <p>At Velloway Advisory, we're dedicated to turning your business aspirations into reality. Our expertise and commitment ensure you make informed, strategic decisions that drive success. Take the first step towards achieving your goals with confidence.</p>
  <a class="btn">GET STARTED</a>
</section>

<div class="abs watermark" style="top:2665px;font-size:160px;line-height:190px">Team</div>
<div class="abs section-head" style="top:2746px"><div class="eyebrow">TEAM</div><h2 style="color:var(--navy)">Our Leadership Team</h2></div>

<article class="member abs" style="left:130px">
  <div class="photo" role="img" aria-label="Portrait of Daniel Oh" style="background:linear-gradient(160deg,#5b4a40,#2c2522)"></div>
  <div class="contacts">
    <span><svg width="12" height="12" viewBox="0 0 24 24" fill="#fff"><path d="M6.6 10.8a15 15 0 006.6 6.6l2.2-2.2c.3-.3.7-.4 1-.2 1.1.4 2.3.6 3.6.6.6 0 1 .4 1 1V20c0 .6-.4 1-1 1A17 17 0 013 4c0-.6.4-1 1-1h3.5c.6 0 1 .4 1 1 0 1.3.2 2.5.6 3.6.1.3 0 .7-.2 1z"/></svg></span>
    <span><svg width="12" height="12" viewBox="0 0 24 24" fill="none" stroke="#fff" stroke-width="2"><rect x="3" y="5" width="18" height="14" rx="1"/><path d="M3 6l9 7 9-7"/></svg></span>
  </div>
  <div class="info">
    <h3>Daniel Oh</h3>
    <div class="role">PRINCIPAL</div>
    <p>Daniel Oh is a seasoned real estate expert with extensive experience in project and construction management, and a licensed real estate agent in California. Fluent in both English and Korean,...</p>
  </div>
</article>
<article class="member abs" style="left:617px">
  <div class="photo" role="img" aria-label="Portrait of Rafael Montoya" style="background:linear-gradient(170deg,#c9d9e8,#8fa7bd 55%,#d9dfe6)"></div>
  <div class="contacts">
    <span><svg width="12" height="12" viewBox="0 0 24 24" fill="#fff"><path d="M6.6 10.8a15 15 0 006.6 6.6l2.2-2.2c.3-.3.7-.4 1-.2 1.1.4 2.3.6 3.6.6.6 0 1 .4 1 1V20c0 .6-.4 1-1 1A17 17 0 013 4c0-.6.4-1 1-1h3.5c.6 0 1 .4 1 1 0 1.3.2 2.5.6 3.6.1.3 0 .7-.2 1z"/></svg></span>
    <span><svg width="12" height="12" viewBox="0 0 24 24" fill="none" stroke="#fff" stroke-width="2"><rect x="3" y="5" width="18" height="14" rx="1"/><path d="M3 6l9 7 9-7"/></svg></span>
  </div>
  <div class="info">
    <h3>Rafael Montoya</h3>
    <div class="role">PRINCIPAL</div>
    <p>Rafael Montoya brings almost 20 years of rich experience as a real estate investor and a pivotal role at one of southern California's largest real estate management firms, where he...</p>
  </div>
</article>

<section class="contact abs">
  <div class="eyebrow">GET IN TOUCH</div>
  <h2>Contact Us</h2>
  <div class="field" style="left:114px;top:193px;width:207px;height:36px">Full Name</div>
  <div class="field" style="left:338px;top:193px;width:209px;height:36px">Company</div>
  <div class="field" style="left:114px;top:249px;width:207px;height:37px">Phone No</div>
  <div class="field" style="left:338px;top:249px;width:209px;height:37px">Email</div>
  <div class="field" style="left:114px;top:303px;width:433px;height:106px;align-items:flex-start;padding-top:18px">Type your message here...</div>
  <a class="btn submit">SUBMIT</a>
</section>
<div class="abs map" role="img" aria-label="Street map showing the office location at 218 Meridian Way, Irvine"></div>

<div class="abs brand footer-brand"><span class="brand-dot"></span><span class="brand-name">Velloway<br>Advisory</span></div>
<div class="abs copy">Copyright © 2024 | <span>Velloway Advisory</span></div>

<div class="abs fcol" style="left:508px;top:3885px">
  <h4>LINKS</h4>
  <ul style="margin-top:10px"><li>About</li><li>Services</li><li>Team</li><li>Contact</li></ul>
</div>
<div class="abs fcol" style="left:670px;top:3885px">
  <h4>CONTACT INFO</h4>
  <div class="line" style="margin-top:16px"><svg width="12" height="16" viewBox="0 0 12 16" fill="#7cc4a3"><path d="M6 0a6 6 0 00-6 6c0 4.5 6 10 6 10s6-5.5 6-10a6 6 0 00-6-6zm0 8.5A2.5 2.5 0 116 3.5a2.5 2.5 0 010 5z"/></svg><span>218 Meridian Way,<br>Irvine, CA 92614</span></div>
  <div class="line"><svg width="12" height="12" viewBox="0 0 24 24" fill="#7cc4a3"><path d="M6.6 10.8a15 15 0 006.6 6.6l2.2-2.2c.3-.3.7-.4 1-.2 1.1.4 2.3.6 3.6.6.6 0 1 .4 1 1V20c0 .6-.4 1-1 1A17 17 0 013 4c0-.6.4-1 1-1h3.5c.6 0 1 .4 1 1 0 1.3.2 2.5.6 3.6.1.3 0 .7-.2 1z"/></svg><span>(949) 555-0187</span></div>
  <div class="line"><svg width="13" height="12" viewBox="0 0 24 24" fill="none" stroke="#7cc4a3" stroke-width="2"><rect x="3" y="5" width="18" height="14" rx="1"/><path d="M3 6l9 7 9-7"/></svg><span>hello@vellowayadvisory.example</span></div>
</div>
<div class="abs fcol" style="left:935px;top:3885px">
  <h4>CONNECT WITH US</h4>
  <div class="social"><span></span><span></span><span></span><span></span></div>
</div>

</body>
</html>
```